Sports Psychology Business Card Design

Need a catchy and unique business card design for our sport psychology practice. We provide mental performance counseling and consulting to performers from all types of industries with a special emphases on athletes.The name of our practice is "Inner Edge of Excellence" or "IEE" as is indicated in the logo examples submitted in this brief. Also provided were logos with specific sports referenced which represent sources of our clients from those sports.

Target Market(s)

Executives, Professionals (doctors, lawyers, etc.), Athletes, Entertainers and other performers

Contact Information for Business Card

Need to include our logo (logos provided in this brief).

Font styles to use
Other font styles liked:
• Font can be found in logo

Colors
0792cd
34a7d8
85cae6

Requirements
Must have
• Our logo and reference to our provision of mental performance counseling/consulting/coaching
Nice to have
• References to sports that our athletes play as provided in the brief.
Should not have
• This is not a general wellness consulting practice. Our focus is on consulting to improve mental performance.

```html
<!DOCTYPE html>
<html lang="en">
<head>
<meta charset="utf-8">
<title>Inner Edge of Excellence – Business Card</title>
<link href="https://fonts.googleapis.com/css2?family=Exo+2:wght@400;600;800&family=Open+Sans:wght@400&display=swap" rel="stylesheet">
<style>
  :root {
    --backdrop: #3b3b39;
    --card: #141517;
    --white: #f4f6f8;
    --blue: #0792cd;
    --blue-mid: #34a7d8;
    --blue-light: #85cae6;
  }
  * { margin: 0; padding: 0; box-sizing: border-box; }
  html, body {
    width: 1200px; height: 824px; overflow: hidden;
    background: var(--backdrop);
  }
  .stage {
    position: relative; width: 1200px; height: 824px;
  }
  .card {
    position: absolute; top: 257px;
    width: 530px; height: 310px;
    background: var(--card);
    border-radius: 4px;
    box-shadow: 0 14px 30px rgba(0,0,0,.45);
  }
  .card--front { left: 50px; }
  .card--back { left: 620px; }

  /* Front */
  .front-mark {
    position: absolute; left: 44px; top: 52px;
    font-family: "Exo 2", sans-serif; font-weight: 800;
    font-size: 44px; letter-spacing: 2px;
    color: var(--blue);
  }
  .tagline {
    position: absolute; right: 44px; top: 150px;
    font-family: "Exo 2", sans-serif; font-weight: 400;
    font-size: 27px; line-height: 1.12; letter-spacing: 1.5px;
    text-transform: uppercase; text-align: right;
    color: var(--white);
  }

  /* Back */
  .brand {
    position: absolute; left: 44px; top: 108px;
    font-family: "Exo 2", sans-serif; font-weight: 800;
    font-size: 60px; letter-spacing: 1px;
    color: var(--white);
  }
  .divider {
    position: absolute; left: 218px; top: 74px;
    width: 1px; height: 156px;
    background: var(--blue-mid);
  }
  .person {
    position: absolute; left: 238px; top: 74px;
  }
  .person-name {
    font-family: "Exo 2", sans-serif; font-weight: 600;
    font-size: 22px; letter-spacing: 1.5px;
    text-transform: uppercase; color: var(--white);
  }
  .person-role {
    margin-top: 2px;
    font-family: "Exo 2", sans-serif; font-weight: 400;
    font-size: 13px; letter-spacing: 1.2px;
    text-transform: uppercase; color: var(--blue-mid);
  }
  .contact-list {
    list-style: none; margin-top: 14px;
    font-family: "Open Sans", sans-serif; font-size: 14px;
    color: var(--white);
  }
  .contact-list li {
    display: flex; align-items: center; gap: 10px;
    height: 24px;
  }
  .contact-list svg { width: 12px; height: 12px; flex: none; }
  .contact-list .handle { color: var(--blue-mid); }
</style>
</head>
<body>
<main class="stage">
  <section class="card card--front" aria-label="Card front">
    <div class="front-mark">IEE</div>
    <p class="tagline">The Inner Edge<br>of Excellence</p>
  </section>

  <section class="card card--back" aria-label="Card back">
    <div class="brand">IEE</div>
    <div class="divider"></div>
    <div class="person">
      <h1 class="person-name">Dana Whitfield</h1>
      <p class="person-role">Mental Performance Consultant</p>
      <ul class="contact-list">
        <li>
          <svg viewBox="0 0 12 12" aria-hidden="true"><path d="M3 1 L5 3.5 L4 5 Q5.5 7.5 7 8 L8.5 7 L11 9 L9.5 11 Q4 10.5 1 3 Z" fill="var(--blue-mid)"/></svg>
          619 404 5127
        </li>
        <li>
          <svg viewBox="0 0 12 12" aria-hidden="true"><rect x="0.5" y="2" width="11" height="8" fill="var(--blue-mid)"/><polyline points="0.5,2 6,6.5 11.5,2" fill="none" stroke="var(--card)" stroke-width="1"/></svg>
          dana@theiee.co
        </li>
        <li>
          <svg viewBox="0 0 12 12" aria-hidden="true"><circle cx="6" cy="6" r="5" fill="none" stroke="var(--blue-mid)" stroke-width="1.2"/><ellipse cx="6" cy="6" rx="2.2" ry="5" fill="none" stroke="var(--blue-mid)" stroke-width="1"/><line x1="1" y1="6" x2="11" y2="6" stroke="var(--blue-mid)" stroke-width="1"/></svg>
          www.theiee.co
        </li>
        <li>
          <svg viewBox="0 0 12 12" aria-hidden="true"><rect x="1" y="1" width="10" height="10" rx="1" fill="var(--blue-mid)"/></svg>
          <span class="handle">_theiee_</span>
        </li>
      </ul>
    </div>
  </section>
</main>
</body>
</html>
```